New church needs a postcard design to promote free community event for hunters

We are a new church in a rural area of southwest VA- near Brisco State.
We want to reach the hunters, fishermen, and outdoor lovers in our area. We will host a community lunch where we will serve free food, have a bow-hunting seminar, have some encouraging coaching, and give away prizes including a full-sized ATV (picture attached), a new bow- I forget the brand, a trailer, many more door prizes.
I would love to see: dark graphics and backgrounds with reverse font (light text on dark background- neon bright orange or yellow for the text would be great).
We also would like big images including: some type of deer head, a silhouette of a bow-hunter, and the ATV we're giving away would all be great.
Even though we want it to be postcard size, it will be handed out and not mailed, so feel free to use all of both sides.
The basic information:
date: September 19, 2015
time: 11:30 AM
location: Upper Caldwin High School
Please register for prizes at www.lanternhvx.com/outdoors
At the bottom, I'd like it to say: hosted by Lantern Church and have our logo (attached).

Thanks!

Church

```html
<!DOCTYPE html>
<html lang="en">
<head>
<meta charset="utf-8">
<title>Outdoors Community Lunch – Lantern Church</title>
<link href="https://fonts.googleapis.com/css2?family=Questrial&family=Alfa+Slab+One&display=swap" rel="stylesheet">
<style>
  :root {
    --frame: #e6e6e6;
    --card: #2d2d2d;
    --card-edge: #1f1f1f;
    --band: rgba(176, 108, 66, 0.62);
    --icon: #ef8c4c;
    --label: #ffffff;
    --value: #f4e336;
    --tab: #242424;
    --tab-edge: #5a5a5a;
    --paper: #fbfbfb;
    --silhouette: #0e0e0e;
  }
  * { box-sizing: border-box; margin: 0; padding: 0; }
  html, body { width: 1200px; height: 931px; overflow: hidden; background: var(--frame); }
  .postcard {
    position: absolute; left: 33px; top: 30px; width: 1134px; height: 864px;
    background: radial-gradient(ellipse at 50% 45%, #3a3a3a 0%, var(--card) 55%, var(--card-edge) 100%);
    overflow: hidden;
    font-family: "Questrial", "Century Gothic", sans-serif;
  }
  .activity-band {
    position: absolute; left: 0; top: 90px; width: 100%; height: 114px;
    background: var(--band);
  }
  .activity-icon { position: absolute; top: 104px; width: 90px; height: 90px; }
  .icon-lunch { left: 75px; }
  .icon-bow { left: 295px; }
  .icon-prize { left: 745px; }
  .icon-party { left: 935px; }
  .deer-head {
    position: absolute; left: 486px; top: 30px; width: 162px; height: 370px;
    background: var(--silhouette);
    border-radius: 40px 40px 70px 70px;
  }
  .giveaway-tab {
    position: absolute; left: 790px; top: 428px; width: 380px; height: 68px;
    background: var(--tab); border: 3px solid var(--tab-edge);
    border-radius: 34px 0 0 34px;
    color: #ffffff; font-family: "Alfa Slab One", serif; font-size: 30px;
    line-height: 62px; padding-left: 40px; letter-spacing: 1px;
  }
  .atv-print {
    position: absolute; left: 745px; top: 525px; width: 352px; height: 330px;
    background: var(--paper); padding: 18px 18px 40px;
    transform: rotate(-8deg);
    box-shadow: 4px 6px 14px rgba(0,0,0,0.55);
  }
  .atv-photo {
    width: 100%; height: 100%;
    background: linear-gradient(160deg, #c9ccc4 0%, #8e9485 45%, #3b4431 75%, #2b2f26 100%);
  }
  .event-details { position: absolute; left: 81px; top: 608px; }
  .detail { font-size: 31px; line-height: 35px; display: flex; }
  .detail dt { color: var(--label); width: 150px; }
  .detail dd { color: var(--value); }
  .register { position: absolute; left: 81px; top: 740px; color: var(--label); font-size: 22px; }
  .register span { color: var(--value); }
  .host { position: absolute; left: 81px; top: 790px; display: flex; align-items: center; gap: 18px; }
  .host-line { color: var(--value); font-size: 30px; }
  .church-mark { display: flex; align-items: center; gap: 8px; background: #ffffff; padding: 6px 10px; }
  .church-mark i { width: 18px; height: 18px; background: #d23a2a; display: block; }
  .church-mark b { font-weight: 400; color: #2d2d2d; font-size: 20px; }
</style>
</head>
<body>
<main class="postcard">
  <div class="activity-band"></div>

  <svg class="activity-icon icon-lunch" viewBox="0 0 90 90" aria-label="Free lunch">
    <g fill="none" stroke="var(--icon)" stroke-width="5">
      <circle cx="45" cy="48" r="26"/><circle cx="45" cy="48" r="17"/>
    </g>
    <g fill="var(--icon)">
      <rect x="5" y="12" width="4" height="24"/><rect x="12" y="12" width="4" height="24"/>
      <rect x="5" y="34" width="11" height="6"/><rect x="8" y="38" width="5" height="44"/>
      <path d="M78 10 q10 14 0 36 v36 h-5 v-72z"/>
    </g>
  </svg>

  <svg class="activity-icon icon-bow" viewBox="0 0 90 90" aria-label="Bow-hunting seminar">
    <g fill="none" stroke="var(--icon)" stroke-width="5" stroke-linecap="round">
      <path d="M20 12 Q70 20 78 70"/>
      <line x1="20" y1="12" x2="78" y2="70" stroke-width="2"/>
      <line x1="12" y1="80" x2="70" y2="22"/>
    </g>
    <path d="M70 22 l-14 2 l12 12z" fill="var(--icon)"/>
  </svg>

  <div class="deer-head" role="img" aria-label="Black silhouette of a deer head with antlers"></div>

  <svg class="activity-icon icon-prize" viewBox="0 0 90 90" aria-label="Prizes">
    <g fill="var(--icon)">
      <path d="M25 10 h40 v18 q0 24 -20 26 q-20 -2 -20 -26z"/>
      <rect x="40" y="54" width="10" height="14"/>
      <rect x="28" y="68" width="34" height="12"/>
    </g>
    <g fill="none" stroke="var(--icon)" stroke-width="5">
      <path d="M25 16 h-12 q0 20 16 22"/><path d="M65 16 h12 q0 20 -16 22"/>
    </g>
  </svg>

  <svg class="activity-icon icon-party" viewBox="0 0 90 90" aria-label="Celebration">
    <g fill="var(--icon)">
      <ellipse cx="30" cy="30" rx="15" ry="19"/>
      <ellipse cx="58" cy="26" rx="15" ry="19"/>
      <ellipse cx="45" cy="44" rx="13" ry="16"/>
    </g>
    <g fill="none" stroke="var(--icon)" stroke-width="2">
      <path d="M30 49 L45 84 M58 45 L45 84 M45 60 L45 84"/>
    </g>
  </svg>

  <div class="giveaway-tab">ATV GIVEAWAY!</div>

  <figure class="atv-print">
    <div class="atv-photo" role="img" aria-label="Photo of the full-sized ATV being given away"></div>
  </figure>

  <dl class="event-details">
    <div class="detail"><dt>Date:</dt><dd>September 19, 2015</dd></div>
    <div class="detail"><dt>Time:</dt><dd>11:30 AM</dd></div>
    <div class="detail"><dt>Location:</dt><dd>Upper Caldwin High School</dd></div>
  </dl>

  <p class="register">Please register for prizes at <span>www.lanternhvx.com/outdoors</span></p>

  <div class="host">
    <p class="host-line">Hosted by: Lantern Church.</p>
    <div class="church-mark"><i></i><b>Lantern Church</b></div>
  </div>
</main>
</body>
</html>
```